Eye Catching Stylish Seminar Flyer

Design a Business Seminar Flyer that will be used for Print and Web distribution that is professional, eye catching in its color scheme and fonts.

have www.brightledgerday.com to register

Target Market(s)

Who is this for: business owners, marketplace professionals, homemakers.

Industry/Entity Type

Business Consultant

Font styles to use
Serif

Colors
abd037

Requirements
Must have
• Great colors, great Font
Nice to have
• Design a simple professional text based Logo for the Event that encapsulates For the flyer. Eye catching designs that provoke action in the reader of the flyer.
Should not have
• Cross designs stereotypical designs that are associated with religion. Rather they should be creative toward people that own businesses and work with colleagues in a daily office, school etc.

```html
<!DOCTYPE html>
<html lang="en">
<head>
<meta charset="utf-8">
<title>The Voice of the Lord in the Marketplace – Seminar Flyer</title>
<link href="https://fonts.googleapis.com/css2?family=Anton&family=Oswald:wght@300;400;500;600;700&family=Kalam:wght@700&display=swap" rel="stylesheet">
<style>
  :root{
    --maroon:#7b1c2e;
    --rust:#c84f2e;
    --ink:#231f20;
    --gold:#fcd64a;
    --gold-deep:#f8c437;
    --cream:#fdf8d8;
    --white:#ffffff;
  }
  html,body{margin:0;padding:0;width:1200px;height:1000px;overflow:hidden;background:var(--white);}
  .flyer{
    position:absolute;left:246px;top:0;width:707px;height:1000px;overflow:hidden;
    font-family:'Oswald',sans-serif;text-align:center;
  }
  .hero{
    position:absolute;left:0;top:0;width:100%;height:485px;
    background:radial-gradient(ellipse at 50% 42%, #fffef2 0%, var(--cream) 30%, #f7eab0 65%, #e9d79a 100%);
  }
  .line{position:absolute;left:0;width:100%;margin:0;}
  .presenter{top:28px;font-weight:700;font-size:38px;line-height:44px;color:var(--maroon);letter-spacing:-0.5px;}
  .presenter span{color:var(--rust);}
  .title{
    font-family:'Anton',sans-serif;color:var(--gold);
    -webkit-text-stroke:5px var(--ink);paint-order:stroke fill;
    text-shadow:6px 6px 0 var(--ink);
  }
  .title-top{top:62px;font-size:100px;line-height:110px;transform:scaleX(1.12);}
  .title-mid{top:172px;height:52px;display:flex;align-items:center;justify-content:center;gap:14px;}
  .title-mid .rule{width:142px;height:7px;border-radius:4px;background:var(--ink);}
  .title-mid span{font-family:'Anton',sans-serif;font-size:46px;line-height:52px;color:var(--ink);}
  .title-main{top:214px;font-size:132px;line-height:140px;transform:scaleX(1.42);}
  .marketplace{top:352px;font-weight:700;font-size:54px;line-height:64px;color:var(--maroon);letter-spacing:-1px;}
  .tagline{top:410px;font-weight:500;font-size:44px;line-height:58px;color:var(--rust);letter-spacing:-1.5px;}
  .band{position:absolute;left:0;width:100%;color:var(--white);font-weight:700;display:flex;align-items:center;justify-content:center;gap:34px;letter-spacing:-0.5px;}
  .band sup{font-size:0.5em;vertical-align:0.8em;}
  .band-day1{top:485px;height:63px;background:var(--maroon);font-size:40px;}
  .band-day2{top:548px;height:60px;background:var(--rust);font-size:40px;}
  .details{
    position:absolute;left:0;top:608px;width:100%;height:342px;
    background:radial-gradient(ellipse at 50% 35%, #fff6c8 0%, #fde98a 40%, var(--gold-deep) 100%);
  }
  .location{top:22px;height:30px;display:flex;align-items:center;justify-content:center;gap:20px;}
  .location .rule{flex:1;height:5px;background:var(--ink);border-radius:3px;}
  .location .rule.left{margin-left:-2px;}
  .location p{margin:0;font-weight:600;font-size:25px;color:var(--white);-webkit-text-stroke:4px var(--ink);paint-order:stroke fill;letter-spacing:-0.5px;}
  .featuring{top:56px;font-weight:700;font-size:27px;line-height:34px;color:var(--ink);}
  .speakers{position:absolute;top:88px;left:0;width:100%;margin:0;padding:0;list-style:none;}
  .speakers li{height:30px;line-height:30px;}
  .speaker-name{font-family:'Kalam',cursive;font-weight:700;font-size:25px;color:var(--maroon);}
  .speaker-role{font-weight:300;font-size:19px;color:var(--rust);}
  .speaker-role::before{content:"•";color:var(--ink);font-weight:700;margin:0 8px 0 6px;}
  .fee{top:244px;font-weight:600;font-size:22px;line-height:30px;color:var(--ink);letter-spacing:-0.4px;}
  .register{top:310px;font-weight:600;font-size:22px;line-height:30px;color:var(--ink);letter-spacing:-0.3px;}
  .footer{position:absolute;left:0;top:950px;width:100%;height:50px;background:var(--maroon);color:var(--white);font-weight:700;font-size:28px;line-height:50px;letter-spacing:-0.3px;}
</style>
</head>
<body>
<main class="flyer">
  <section class="hero" role="img" aria-label="Radiating cream and gold sunburst backdrop">
    <p class="line presenter">NORTHGATE LEADERS CO. <span>PRESENTS</span></p>
    <h1 class="line title title-top">THE VOICE</h1>
    <div class="line title-mid"><i class="rule"></i><span>OF THE</span><i class="rule"></i></div>
    <p class="line title title-main">LORD</p>
    <h2 class="line marketplace">IN THE MARKETPLACE:</h2>
    <p class="line tagline">Moving from Intimacy to Impact</p>
  </section>

  <div class="band band-day1"><span>MARCH 24<sup>th</sup></span><span>6:00<sup>pm</sup> - 9:20<sup>pm</sup></span></div>
  <div class="band band-day2"><span>MARCH 25<sup>th</sup></span><span>8:30<sup>am</sup> - 2:20<sup>pm</sup></span></div>

  <section class="details">
    <div class="line location"><i class="rule left"></i><p>LOCATION:&nbsp; Riverside Community Hall</p><i class="rule"></i></div>
    <p class="line featuring">FEATURING</p>
    <ul class="speakers">
      <li><span class="speaker-name">Marcus Hale</span><span class="speaker-role">Author/Podcaster</span></li>
      <li><span class="speaker-name">Owen Park</span><span class="speaker-role">Venture Partner</span></li>
      <li><span class="speaker-name">Celia Hale</span><span class="speaker-role">Writer</span></li>
      <li><span class="speaker-name">Rosa Medina</span><span class="speaker-role">Business Owner</span></li>
      <li><span class="speaker-name">Thomas Reed</span><span class="speaker-role">Business Owner</span></li>
    </ul>
    <p class="line fee">FEE: $30 • Includes continental breakfast, lunch and light refreshments<br>throughout the conference.</p>
    <p class="line register">Register at www.brightledgerday.com</p>
  </section>

  <footer class="footer">BRINGING GOD A RETURN ON HIS INVESTMENT</footer>
</main>
</body>
</html>
```